Design a "healthy, happy dog and cat" cheque/check background

I am looking for a few design concepts featuring a happy healthy dog and cat, that will be used as the background of a paper cheque/check.

This will require Photoshop and stock photos.

Here is the design brief: https://files.brivontel.net/sheet/48kQmZ2xTrWvLpN7aHcYeJ5uBdFsKo9GiRtXnVw3Lz/view?share=on

Colors

Designer to choose colors to be used in the design.

Requirements
Must have
• A happy dog and cat the main focus within the "empty" central part of the cheque/check, and a complementary background for the rest of the cheque, following the design guidelines in the attached google doc.

```html
<!DOCTYPE html>
<html lang="en">
<head>
<meta charset="utf-8">
<title>Northvale Cheques Personal Cheque</title>
<link rel="stylesheet" href="https://fonts.googleapis.com/css2?family=Arimo:wght@400;700&family=Share+Tech+Mono&display=swap">
<style>
  :root {
    --page: #f4f2f3;
    --ink: #1c1a1c;
    --panel: rgba(255, 255, 255, 0.62);
    --field: #ffffff;
    --photo-cat: #6f6a74;
    --photo-mauve: #9c8795;
    --photo-dog: #b9713f;
    --photo-floor: #e6dcd8;
    --micr-band: #f1eeee;
    --rule: #2a2628;
  }
  * { box-sizing: border-box; margin: 0; padding: 0; }
  html, body {
    width: 1200px; height: 544px; overflow: hidden;
    background: var(--page);
    font-family: "Arimo", Arial, sans-serif;
    color: var(--ink);
  }
  .cheque { position: relative; width: 1200px; height: 544px; }
  .cheque-photo {
    position: absolute; left: 24px; top: 20px; width: 1148px; height: 392px;
    background:
      radial-gradient(ellipse 320px 240px at 340px 220px, var(--photo-cat) 0%, rgba(111,106,116,0) 100%),
      radial-gradient(ellipse 360px 260px at 720px 250px, var(--photo-dog) 0%, rgba(185,113,63,0) 100%),
      linear-gradient(180deg, #b8a6b1 0%, var(--photo-mauve) 55%, #7b6a72 100%);
  }
  .micr-band {
    position: absolute; left: 24px; top: 412px; width: 1148px; height: 108px;
    background: linear-gradient(180deg, var(--photo-floor) 0%, var(--micr-band) 60%);
  }
  .panel { position: absolute; background: var(--panel); }
  .account-holder { left: 56px; top: 54px; width: 474px; height: 88px; padding: 8px 0 0 2px; }
  .account-holder .title { font-size: 21px; font-weight: 700; color: #2b2a2c; }
  .account-holder .line { font-size: 19px; line-height: 21px; color: #2b2a2c; }
  .cheque-number { position: absolute; left: 1024px; top: 46px; font-size: 23px; font-weight: 700; }
  .date-label { position: absolute; left: 784px; top: 110px; font-size: 20px; }
  .date-boxes { position: absolute; left: 848px; top: 90px; display: flex; gap: 2px; }
  .date-box { width: 37px; height: 36px; background: var(--field); }
  .date-format { position: absolute; left: 848px; top: 131px; display: flex; gap: 2px; }
  .date-format span { width: 37px; text-align: center; font-size: 13px; }
  .payee { left: 50px; top: 180px; width: 878px; height: 98px; }
  .pay-label { position: absolute; left: 58px; top: 190px; font-size: 14px; line-height: 13px; }
  .dollar-sign { position: absolute; left: 952px; top: 188px; font-size: 28px; }
  .amount-box { position: absolute; left: 972px; top: 175px; width: 194px; height: 48px; background: var(--field); }
  .dollars-label { position: absolute; left: 918px; top: 253px; font-size: 13px; }
  .bank { left: 50px; top: 288px; width: 467px; height: 86px; }
  .bank-mark { position: absolute; left: 62px; top: 300px; width: 40px; height: 40px; background: #2c2a2c; }
  .bank-text { position: absolute; left: 154px; top: 297px; font-size: 16px; line-height: 19px; }
  .bank-text .name { font-size: 18px; font-weight: 700; }
  .company-name { position: absolute; left: 810px; top: 333px; font-size: 13px; }
  .memo-label { position: absolute; left: 60px; top: 385px; font-size: 10px; }
  .security-badge {
    position: absolute; left: 1162px; top: 272px; width: 30px; height: 134px;
    border: 1px solid #555; border-radius: 4px; background: rgba(255,255,255,0.35);
  }
  .micr-line {
    position: absolute; left: 56px; top: 450px;
    font-family: "Share Tech Mono", monospace; font-size: 26px; letter-spacing: 3px; color: #111;
  }
  .rules { position: absolute; left: 0; top: 0; }
</style>
</head>
<body>
<main class="cheque">
  <div class="cheque-photo" role="img" aria-label="Photo of a grey and white cat lying beside a golden retriever on a pale floor"></div>
  <div class="micr-band"></div>

  <section class="panel account-holder">
    <p class="title">Northvale Cheques Personal Cheque</p>
    <p class="line">15 Residential Street</p>
    <p class="line">Toronto, Ontario M1M 1M1</p>
  </section>

  <div class="cheque-number">101</div>
  <div class="date-label">DATE</div>
  <div class="date-boxes">
    <span class="date-box"></span><span class="date-box"></span><span class="date-box"></span><span class="date-box"></span>
    <span class="date-box"></span><span class="date-box"></span><span class="date-box"></span><span class="date-box"></span>
  </div>
  <div class="date-format"><span>D</span><span>D</span><span>M</span><span>M</span><span>Y</span><span>Y</span><span>Y</span><span>Y</span></div>

  <div class="panel payee"></div>
  <div class="pay-label">PAY TO THE<br>ORDER OF</div>
  <div class="dollar-sign">$</div>
  <div class="amount-box"></div>
  <div class="dollars-label">100 DOLLARS</div>

  <section class="panel bank"></section>
  <div class="bank-mark"></div>
  <div class="bank-text">
    <p class="name">Your Financial Institution</p>
    <p>200 Finance Avenue</p>
    <p>Your City, Your Province A1B 2CS</p>
  </div>

  <div class="company-name">Optional Company Name</div>
  <div class="memo-label">MEMO</div>
  <div class="security-badge"></div>

  <svg class="rules" width="1200" height="544" viewBox="0 0 1200 544">
    <g stroke="var(--rule)" stroke-width="1" fill="none">
      <polyline points="140,222 920,222 922,194"/>
      <polyline points="58,276 904,276 910,248"/>
      <line x1="60" y1="398" x2="584" y2="398"/>
      <line x1="686" y1="398" x2="1098" y2="398"/>
    </g>
  </svg>

  <div class="micr-line">|101|  :12345-678:  12345-6789|</div>
</main>
</body>
</html>
```